DeskWizard.dk Frontpage design

I'm in the process of starting a It-course website, based in Denmark. The web site Url is - www.deskwizard.dk

The services are:
- Online courses (This is the main service and the most important)
- One to One courses
- Webinar

I need a frontpage design a simple design, but it must shows professionalism. I have no preference in color, but I like white space.

In Denmark the established competitors are:
- www.tasniva.dk (Biggest competitor)
- www.bramfeldt.dk/online-kurser
- www.velunda.dk

Target Market(s)

Mainly companies (B to B), but there are also a small number of private customers

Industry/Entity Type

Online it courses and one to one consulting

Number of Pages Required

1 page

Font styles to use
Sans Serif

Requirements
Must have
• A professional design, white space

```html
<!DOCTYPE html>
<html lang="en">
<head>
<meta charset="utf-8">
<title>DeskWizard.dk – Online IT courses</title>
<link rel="stylesheet" href="https://fonts.googleapis.com/css2?family=Poppins:wght@400;500;600;700;800&display=swap">
<style>
:root{
  --green:#22c55e;
  --green-deep:#1fb24f;
  --orange:#e39a16;
  --ink:#111111;
  --dark:#141a16;
  --dark-2:#1b231d;
  --white:#ffffff;
  --muted:#4a4a4a;
}
*{margin:0;padding:0;box-sizing:border-box}
html,body{width:1200px;height:4137px;overflow:hidden}
body{font-family:'Poppins',sans-serif;color:var(--ink);background:var(--white);position:relative}
section,header,footer{position:relative;width:1200px;overflow:hidden}
.abs{position:absolute}
.center{left:0;width:1200px;text-align:center}
.eyebrow{font-size:13px;font-weight:600;letter-spacing:5px;color:var(--green-deep)}
.title{font-size:34px;font-weight:700;line-height:1.2}
.btn{display:inline-flex;align-items:center;justify-content:center;border-radius:30px;font-size:12px;font-weight:700;text-transform:uppercase;letter-spacing:.3px}
.btn-dark{background:var(--ink);color:var(--white)}
.btn-green{background:var(--green);color:var(--white)}

/* HERO */
.hero{height:721px;background:linear-gradient(100deg,var(--green) 0%,#6fbf38 50%,var(--orange) 100%);color:var(--white)}
.logo{font-size:31px;font-weight:700;color:var(--white)}
.nav{top:68px;left:424px;display:flex;gap:24px;font-size:12px}
.signin{left:875px;top:59px;width:113px;height:40px}
.hero .welcome{left:210px;top:256px;font-size:13px;font-weight:600;letter-spacing:4px}
.hero h1{left:210px;top:284px;font-size:41px;font-weight:700;line-height:49px;width:420px}
.hero p{left:210px;top:450px;font-size:12px;line-height:21px;width:360px}
.get-started{left:210px;top:521px;width:127px;height:40px}
.watch{left:350px;top:519px;display:flex;align-items:center;gap:12px;font-size:12px;font-weight:700}
.watch .play{width:40px;height:40px;border-radius:50%;background:var(--white);display:flex;align-items:center;justify-content:center}
.hero-panel{left:687px;top:257px;width:334px;height:353px;background:#111;border-radius:0 0 170px 170px}
.hero-photo{left:745px;top:158px;width:285px;height:450px;background:linear-gradient(180deg,#3e6fb0,#243f6b);border-radius:140px 140px 150px 150px;opacity:.9}

/* COURSES */
.courses{height:508px}
.courses .eyebrow{top:79px}
.courses .title{top:106px}
.courses .sub{top:152px;font-size:15px;color:var(--muted)}
.card{border-radius:8px;overflow:hidden;background:linear-gradient(160deg,#3b3f3c,#171a18);color:var(--white);box-shadow:0 10px 30px rgba(0,0,0,.15)}
.card .price{position:absolute;left:16px;top:0;background:var(--white);color:var(--ink);font-weight:700;font-size:14px;line-height:16px;padding:10px 10px 8px;border-radius:0 0 6px 6px}
.card .badge{position:absolute;width:60px;height:60px;border-radius:50%;background:var(--white)}
.card-body{position:absolute;left:22px;right:22px;bottom:14px;display:flex;flex-direction:column}
.card-body h3{font-weight:700;font-size:14px;line-height:18px}
.card-body p{margin-top:4px;font-size:10px;line-height:16px;color:#e5e5e5}
.card-foot{margin-top:10px;display:flex;align-items:center;justify-content:space-between}
.tags{display:flex;gap:6px}
.tag{background:#8a8f8b;color:var(--white);font-size:9px;font-weight:700;border-radius:10px;padding:2px 10px;text-transform:uppercase}
.c1{left:151px;top:239px;width:279px;height:196px}
.c2{left:445px;top:219px;width:310px;height:217px}
.c2 .card-body h3{font-size:17px;line-height:21px}
.c2 .card-body p{font-size:11px;line-height:17px}
.c3{left:769px;top:239px;width:280px;height:196px}

/* WHY */
.why{height:552px;background:linear-gradient(180deg,var(--dark),#1d241f 60%,#101411);color:var(--white)}
.why .eyebrow{top:72px}
.why .title{top:99px}
.why .sub{top:141px;font-size:12px}
.feature{top:220px;width:180px;height:181px;border-radius:6px;background:var(--dark-2);border-left:2px solid var(--green);border-bottom:2px solid var(--green);text-align:center;padding-top:35px}
.feature.active{background:linear-gradient(135deg,var(--green),#9aaa2b);border:3px solid var(--white)}
.feature .ic{width:56px;height:56px;margin:0 auto 14px;border-radius:50%;background:var(--white);display:flex;align-items:center;justify-content:center}
.feature span{font-size:19px;font-weight:500;line-height:22px;display:block}
.about{left:536px;top:435px;width:127px;height:38px}

/* WEBINAR */
.webinar{height:797px}
.webinar .eyebrow{top:72px}
.webinar .title{top:100px}
.webinar .lead{top:151px;left:310px;width:580px;font-size:12px;line-height:21px;color:var(--muted);text-align:center}
.desk-scene{left:0;top:245px;width:1200px;height:470px;background:radial-gradient(ellipse at center,#e7ebee 0%,#f4f5f6 45%,#ffffff 75%)}
.screen{left:356px;top:260px;width:460px;height:255px;border-radius:8px;background:linear-gradient(90deg,#1d3348,#4c6680 55%,#c8c9cc);border:10px solid #1a1a1a}
.webplay{left:548px;top:350px;width:80px;height:80px;border-radius:50%;background:var(--white);display:flex;align-items:center;justify-content:center}

/* BLOG */
.blog{height:724px;background:linear-gradient(180deg,#0f1411,#1c231e 55%,#121713);color:var(--white)}
.blog .eyebrow{top:82px}
.blog .title{top:110px}
.post{top:181px;width:257px}
.post .img{height:172px;border-radius:4px}
.post h3{margin-top:16px;font-size:19px;font-weight:700;line-height:24px}
.post p{margin-top:10px;font-size:11px;line-height:17px;color:#e3e3e3}
.post .stats{display:flex;gap:40px;margin-top:8px}
.post .stats b{display:block;color:var(--green);font-size:16px;font-weight:700;line-height:18px}
.post .stats small{font-size:8px}
.post .read{margin-top:12px;font-size:11px;font-weight:700}
.more{left:530px;top:591px;width:140px;height:38px}

/* ONE TO ONE */
.onetoone{height:504px}
.banner{left:210px;top:146px;width:779px;height:283px;border-radius:8px;background:linear-gradient(100deg,var(--green),#8dbb2c 60%,var(--orange))}
.banner-title{left:299px;top:197px;font-size:32px;font-weight:700;color:var(--white)}
.banner-text{left:299px;top:250px;width:250px;font-size:12px;line-height:21px;color:var(--white)}
.oto-btn{left:300px;top:331px;width:126px;height:38px}
.person{left:620px;top:48px;width:250px;height:381px;background:linear-gradient(180deg,#7a5a44,#d8d0c2 45%,#b9b9b9);border-radius:120px 120px 0 0;opacity:.85}

/* FOOTER */
.footer{height:331px;background:#141414;color:var(--white)}
.footer .logo{left:210px;top:62px}
.footer .about-text{left:210px;top:120px;width:230px;font-size:12px;line-height:22px}
.col{top:112px;font-size:12px}
.col h4{font-size:14px;font-weight:600;margin-bottom:8px}
.col li{list-style:none;line-height:27px}
.contact-row{display:flex;align-items:center;gap:14px;margin-bottom:22px;font-size:12px;line-height:14px}
.dot{width:24px;height:24px;border-radius:50%;background:var(--green);display:flex;align-items:center;justify-content:center;flex:none}
.copyright{left:0;top:284px;width:1200px;height:47px;background:#3a3a3a;text-align:center;line-height:47px;font-size:11px;font-weight:600}
</style>
</head>
<body>

<header class="hero">
  <div class="abs logo" style="left:210px;top:58px">DeskWizard</div>
  <nav class="abs nav"><span>Kurser</span><span>Webinar</span><span>En til En</span><span>Spørgsmål</span><span>Blog</span><span>Om</span><span>Kontakt</span></nav>
  <a class="abs btn btn-dark signin">Sign in</a>
  <div class="abs welcome">WELCOME TO DESKWIZARD</div>
  <h1 class="abs">Expand Your<br>Skills Define Your<br>Future.</h1>
  <p class="abs">I offer online courses and webinars with a clear focus, or what about online "One to One" teaching</p>
  <a class="abs btn btn-dark get-started">Get started</a>
  <div class="abs watch"><span class="play"><svg width="10" height="12" viewBox="0 0 10 12"><path d="M0 0L10 6L0 12Z" fill="#22c55e"/></svg></span>WATCH OUR VIDEO</div>
  <div class="abs hero-panel"></div>
  <div class="abs hero-photo" role="img" aria-label="Smiling man in a blue shirt holding an open laptop"></div>
</header>

<section class="courses">
  <div class="abs center eyebrow">OUR COURSES</div>
  <div class="abs center title">Selected Courses</div>
  <div class="abs center sub">Find your next online course here</div>

  <article class="abs card c1" role="img" aria-label="Course card over a dim classroom photo">
    <div class="price">199<br>KR.</div>
    <div class="badge" style="right:24px;top:20px"></div>
    <div class="card-body">
      <h3>Dashly BI in one hour</h3>
      <p>Is it possible to learn Dashly BI in just one hour? Probably not, but I can give you an</p>
      <div class="card-foot"><div class="tags"><span class="tag">Dashly BI</span></div>
        <svg width="20" height="10" viewBox="0 0 20 10"><path d="M0 5H18M14 1L18 5L14 9" stroke="#fff" stroke-width="1.5" fill="none"/></svg></div>
    </div>
  </article>

  <article class="abs card c2" role="img" aria-label="Course card over a photo of a developer at a computer">
    <div class="price" style="font-size:18px;line-height:21px">499<br>KR.</div>
    <div class="badge" style="right:26px;top:22px;width:62px;height:62px"></div>
    <div class="card-body">
      <h3>Serpent Script for Gridsheet users</h3>
      <p>How do you as Gridsheet users get started using Serpent Script</p>
      <div class="card-foot"><div class="tags"><span class="tag">Serpent</span><span class="tag">Gridsheet</span></div>
        <svg width="22" height="10" viewBox="0 0 22 10"><path d="M0 5H20M16 1L20 5L16 9" stroke="#fff" stroke-width="1.5" fill="none"/></svg></div>
    </div>
  </article>

  <article class="abs card c3" role="img" aria-label="Course card over a photo of people at computers">
    <div class="price">499<br>KR.</div>
    <div class="badge" style="right:24px;top:20px"></div>
    <div class="card-body">
      <h3>Stat-Q Introduction</h3>
      <p>Introduction to Stat-Q programming.</p>
      <div class="card-foot"><div class="tags"><span class="tag">Serpent</span></div>
        <svg width="20" height="10" viewBox="0 0 20 10"><path d="M0 5H18M14 1L18 5L14 9" stroke="#fff" stroke-width="1.5" fill="none"/></svg></div>
    </div>
  </article>
</section>

<section class="why">
  <div class="abs center eyebrow">why choose us</div>
  <div class="abs center title">Why DeskWizard?</div>
  <div class="abs center sub">I have been teaching a lot of happy students since 1995.</div>

  <div class="abs feature" style="left:209px"><div class="ic"><svg width="26" height="26" viewBox="0 0 26 26"><circle cx="13" cy="11" r="6" fill="#f2c230"/><rect x="10" y="17" width="6" height="4" fill="#6bbf3a"/></svg></div><span>Why<br>wait</span></div>
  <div class="abs feature active" style="left:408px"><div class="ic"><svg width="30" height="30" viewBox="0 0 30 30"><circle cx="15" cy="15" r="14" fill="#22c55e"/><text x="15" y="21" text-anchor="middle" font-family="Poppins,sans-serif" font-weight="700" font-size="17" fill="#fff">$</text></svg></div><span>Good<br>Economy</span></div>
  <div class="abs feature" style="left:605px"><div class="ic"><svg width="30" height="30" viewBox="0 0 30 30"><circle cx="15" cy="15" r="13" fill="#3aa84a"/><path d="M8 10Q15 6 22 12M6 17Q15 22 24 16" stroke="#fff" stroke-width="2" fill="none"/></svg></div><span>No travel<br>time</span></div>
  <div class="abs feature" style="left:809px"><div class="ic"><svg width="30" height="30" viewBox="0 0 30 30"><path d="M15 3A12 12 0 1 0 15 27C18 27 17 23 20 22S27 21 27 15A12 12 0 0 0 15 3Z" fill="#6bbf3a"/><circle cx="10" cy="12" r="2" fill="#fff"/><circle cx="16" cy="9" r="2" fill="#fff"/><circle cx="9" cy="19" r="2" fill="#fff"/></svg></div><span>Designed<br>in a browser</span></div>

  <a class="abs btn btn-green about">About</a>
</section>

<section class="webinar">
  <div class="abs center eyebrow">Our Videos</div>
  <div class="abs center title">Webinar</div>
  <p class="abs lead">It is not only on the price that webinars beat traditional courses! You get the same high quality in a webinar as in a traditional course, even with the advantage that you can watch them again and again.Best of all, you do not have to move to gain new knowledge</p>
  <div class="abs desk-scene" role="img" aria-label="White desk scene with a desktop computer, lamp, teapot and headphones"></div>
  <div class="abs screen" role="img" aria-label="Video still of a woman working at a computer with code on screen"></div>
  <div class="abs webplay"><svg width="18" height="20" viewBox="0 0 18 20"><path d="M0 0L18 10L0 20Z" fill="#22c55e"/></svg></div>
</section>

<section class="blog">
  <div class="abs center eyebrow">Our Blogs</div>
  <div class="abs center title">Latest Blog Posts</div>

  <article class="abs post" style="left:194px">
    <div class="img" role="img" aria-label="Man in an office reading a tablet" style="background:linear-gradient(135deg,#c9d6e2,#5f7fa0)"></div>
    <h3>Current sum</h3>
    <p>You need to create a current sum over your Gridsheet data. It can do in several different ways.</p>
    <div class="stats"><div><b>52</b><small>Lorem ipsum</small></div><div><b>256</b><small>Lorem ipsum</small></div></div>
    <div class="read">READ THE ARTICLE</div>
  </article>

  <article class="abs post" style="left:471px">
    <div class="img" role="img" aria-label="Spreadsheet app illustration on green gradient" style="background:linear-gradient(135deg,var(--green),#a6a52a)"></div>
    <h3>Use Dashly BI data in Gridsheet</h3>
    <p>Dashly BI is a great program for analyzing, viewing and sharing your report</p>
    <div class="stats"><div><b>52</b><small>Lorem ipsum</small></div><div><b>256</b><small>Lorem ipsum</small></div></div>
    <div class="read">READ THE ARTICLE</div>
  </article>

  <article class="abs post" style="left:748px">
    <div class="img" role="img" aria-label="Laptop showing dashboard charts" style="background:linear-gradient(135deg,#eef2f6,#8ea6c8)"></div>
    <h3>Data from Dashly BI in SlideDeck – Interactive</h3>
    <p>Do you know it - You have created a dashboard in Dashly BI that you must</p>
    <div class="stats"><div><b>52</b><small>Lorem ipsum</small></div><div><b>256</b><small>Lorem ipsum</small></div></div>
    <div class="read">READ THE ARTICLE</div>
  </article>

  <a class="abs btn btn-green more">More articles</a>
</section>

<section class="onetoone">
  <div class="abs banner"></div>
  <div class="abs person" role="img" aria-label="Smiling young man with glasses holding a laptop"></div>
  <h2 class="abs banner-title">One To One</h2>
  <p class="abs banner-text">Targeted teaching at just the right time will make you better and faster for your assignments</p>
  <a class="abs btn btn-dark oto-btn">One to one</a>
</section>

<footer class="footer">
  <div class="abs logo">DeskWizard</div>
  <p class="abs about-text">Lorem ipsum dolor sit amet, consectetur adipiscing elit, sed do eiusmod tempor incididunt ut labore et dolore magna aliqua.</p>
  <div class="abs col" style="left:502px"><h4>Quicks Links</h4><ul><li>Home</li><li>Courses</li><li>Webinar</li><li>One to one</li><li>Questions</li></ul></div>
  <div class="abs col" style="left:655px"><h4>Resources</h4><ul><li>Blog</li><li>About</li><li>Contact</li><li>Terms</li></ul></div>
  <div class="abs col" style="left:821px"><h4>Contact Us</h4>
    <div class="contact-row"><span class="dot"><svg width="10" height="13" viewBox="0 0 10 13"><path d="M5 0A5 5 0 0 0 0 5C0 9 5 13 5 13S10 9 10 5A5 5 0 0 0 5 0Z" fill="#fff"/><circle cx="5" cy="5" r="2" fill="#22c55e"/></svg></span><span>0000 somewhere st.<br>000 somewhere</span></div>
    <div class="contact-row"><span class="dot"><svg width="12" height="12" viewBox="0 0 12 12"><path d="M2 0L4 3L3 4.5Q4.5 7.5 7.5 9L9 8L12 10L10.5 12Q4 11 0 1.5Z" fill="#fff"/></svg></span><span>(012) 3456 7890</span></div>
  </div>
  <div class="abs copyright">COPYRIGHT © DESKWIZARD . ALL RIGHTS RESERVED.</div>
</footer>

</body>
</html>
```